Roofing Company needs Business card design

We need a business card design for our roofing contracting company. We do Residential and commercial roofing. Design need to be modern, professional and clean. The design should communicate quality and professionalism. We would like to have rounded corners, but open to your ideas.
Company Name: Kestrel roofing Solutions
Company Address: (dummy text)
Name on business card: (dummy text)
And following lines:
Storm damage specialists
commercial & residential
shingles, flat and metal roofs./
Open to background colors.
I have ai. and eps files of logo if needed.
just let me know.
Target Market(s)
Mostly residential customers but we do commercial too.
Industry/Entity Type
Roofing
Look and feel

```html
<!DOCTYPE html>
<html lang="en">
<head>
<meta charset="utf-8">
<title>Kestrel roofing Solutions – Business Card</title>
<link rel="stylesheet" href="https://fonts.googleapis.com/css2?family=Questrial&display=swap">
<style>
  :root {
    --stage: #c9cacc;
    --card-white: #ffffff;
    --card-black: #141414;
    --card-black-soft: #202020;
    --brand-red: #c8171e;
    --brand-orange: #f26522;
    --band-start: #d81e1e;
    --band-end: #f47c20;
    --ink-dark: #1e1e1e;
    --ink-light: #f2f2f2;
  }
  * { box-sizing: border-box; margin: 0; padding: 0; }
  html, body {
    width: 1200px;
    height: 900px;
    overflow: hidden;
    background: var(--stage);
    font-family: "Questrial", "Century Gothic", sans-serif;
  }
  .canvas {
    position: relative;
    width: 1200px;
    height: 900px;
    display: flex;
    align-items: center;
    justify-content: center;
    gap: 40px;
  }
  .card {
    position: relative;
    width: 525px;
    height: 300px;
    border-radius: 24px;
    overflow: hidden;
    box-shadow: 0 10px 24px rgba(0, 0, 0, 0.25);
  }

  /* Front */
  .card-front { background: var(--card-black); }
  .front-top {
    position: absolute;
    left: 0; top: 0;
    width: 100%;
    height: 148px;
    background: var(--card-white);
  }
  .accent-band {
    position: absolute;
    left: 0; top: 148px;
    width: 100%;
    height: 10px;
    background: linear-gradient(90deg, var(--band-start), var(--band-end));
  }
  .front-bottom {
    position: absolute;
    left: 0; top: 158px;
    width: 100%;
    height: 142px;
    background: linear-gradient(180deg, var(--card-black-soft), var(--card-black));
  }
  .brand {
    position: absolute;
    left: 26px;
    top: 78px;
    display: flex;
    align-items: center;
    gap: 10px;
  }
  .brand-square {
    width: 16px;
    height: 16px;
    background: var(--brand-red);
  }
  .brand-name {
    color: var(--brand-red);
    font-size: 24px;
    letter-spacing: 0.5px;
  }
  .holder {
    position: absolute;
    right: 28px;
    top: 20px;
    text-align: right;
  }
  .holder-name {
    color: var(--brand-red);
    font-size: 24px;
    line-height: 1.1;
  }
  .holder-role {
    color: var(--ink-dark);
    font-size: 15px;
    margin-top: 4px;
  }
  .contact-list {
    position: absolute;
    left: 24px;
    top: 176px;
    list-style: none;
    color: var(--ink-light);
    font-size: 15px;
    line-height: 21px;
  }
  .contact-item {
    display: flex;
    align-items: flex-start;
    gap: 8px;
  }
  .contact-icon {
    width: 13px;
    height: 13px;
    margin-top: 4px;
    flex: none;
    fill: var(--brand-red);
  }
  .contact-text.indent { padding-left: 21px; }

  /* Back */
  .card-back {
    background: radial-gradient(ellipse at 50% 45%, #262626 0%, var(--card-black) 75%);
    display: flex;
    align-items: center;
    justify-content: center;
  }
  .services {
    list-style: none;
    text-align: center;
    color: var(--brand-orange);
    font-size: 18px;
    line-height: 34px;
  }
</style>
</head>
<body>
<main class="canvas">
  <section class="card card-front" aria-label="Business card front">
    <div class="front-top"></div>
    <div class="accent-band"></div>
    <div class="front-bottom"></div>

    <div class="brand">
      <span class="brand-square"></span>
      <span class="brand-name">Kestrel roofing Solutions</span>
    </div>

    <div class="holder">
      <p class="holder-name">Dana Mercer</p>
      <p class="holder-role">Manager</p>
    </div>

    <ul class="contact-list">
      <li class="contact-item">
        <svg class="contact-icon" viewBox="0 0 16 16" aria-hidden="true"><path d="M3.2 1l2.6 3-1.4 1.6c.9 2 2.4 3.5 4.4 4.4L10.4 8.6l3 2.6-1.6 2.8C6.3 13.6 2.4 9.7 1 3.6z"/></svg>
        <span class="contact-text">1584 320 416</span>
      </li>
      <li class="contact-item">
        <svg class="contact-icon" viewBox="0 0 16 16" aria-hidden="true"><path d="M1 3h14v10H1z M2.5 4.5L8 9l5.5-4.5" stroke="#141414" stroke-width="1.2"/></svg>
        <span class="contact-text">info@kestrelroofing.com</span>
      </li>
      <li class="contact-item">
        <svg class="contact-icon" viewBox="0 0 16 16" aria-hidden="true"><circle cx="8" cy="8" r="7"/><path d="M1 8h14M8 1v14M8 1c-3 3-3 11 0 14M8 1c3 3 3 11 0 14" stroke="#141414" stroke-width="1" fill="none"/></svg>
        <span class="contact-text">www.kestrelroofing.com</span>
      </li>
      <li class="contact-item">
        <svg class="contact-icon" viewBox="0 0 16 16" aria-hidden="true"><path d="M8 1L1 8h2v7h4v-4h2v4h4V8h2z"/></svg>
        <span class="contact-text">PO Box 40518,kestrel street</span>
      </li>
      <li class="contact-item">
        <span class="contact-text indent">AL 31204,canada</span>
      </li>
    </ul>
  </section>

  <section class="card card-back" aria-label="Business card back">
    <ul class="services">
      <li>Storm damage specialists</li>
      <li>commercial &amp; residential</li>
      <li>shingles, flat and metal roofs</li>
    </ul>
  </section>
</main>
</body>
</html>
```